Flaschenetiketten-Design in rechteckiger Grundform für Biermanufaktur
Der Kontakt war sehr professionell und angenehm. Wir wurden hilfreich beraten. Auf unser Feedback haben wir in kurzer Zeit jeweils neue Entwürfe erhalten. Die Zusammenarbeit und der Service war deutlich über unseren Vorstellungen. Wir können KorvaneDeck nur weiterempfehlen!
Zielgruppe
Wir repräsentieren eine Bier-Manufaktur in der Gründungsphase und sind auf der Suche nach einem Designvorschlag für die Flaschenetiketten.
Unsere Zielgruppe sind Liebhaber, die auf der Suche nach dem Speziellen und Lokalen sind. Der Biergenuss abseits des Massenmarktes soll im Entwurf sichtbar/transportiert werden. Die Bier-Manufaktur steht zeitgleich für Trend-Kreationen mit bodenständigem Ursprung.
Aufgabenstellung
Die Herkunft der Gründer Familie aus dem Schweizer Kanton Simplon soll im Vordergrund stehen, hierzu bitte das Familienwappen / einzelne Elemente siehe Dateiupload berücksichtigen.
Das Etikett soll eine rechteckige Grundform haben.
Folgende Angaben sollen sich im Etikett wiederfinden:
- Biersorte: 'Lager' (zukünftig soll es möglich sein, Biersorte auf dem Etikett zu wechseln)
Brand: 'Mostly Grafun'
'Biermanufaktur Walliser Ursprungs'
Die Schrift soll klar und nicht zu verspielt sein.

```html
<!DOCTYPE html>
<html lang="de">
<head>
<meta charset="utf-8">
<title>Mostly Grafun – Lagerbier Etikett</title>
<link href="https://fonts.googleapis.com/css2?family=Montserrat:wght@500;600&display=swap" rel="stylesheet">
<style>
  :root {
    --page-bg: #ffffff;
    --label-frame: #c4c4c4;
    --label-bg: #2b2b2b;
    --crest-fill: #c6c6c6;
    --crest-line: #2b2b2b;
    --text-light: #ffffff;
  }
  html, body {
    margin: 0;
    padding: 0;
    width: 844px;
    height: 1200px;
    overflow: hidden;
    background: var(--page-bg);
  }
  .canvas {
    position: relative;
    width: 844px;
    height: 1200px;
  }
  .label {
    position: absolute;
    left: 102px;
    top: 245px;
    width: 640px;
    height: 709px;
    box-sizing: border-box;
    background: var(--label-bg);
    border: 11px solid var(--label-frame);
    font-family: "Montserrat", sans-serif;
    color: var(--text-light);
    text-align: center;
  }
  .label__crest {
    position: absolute;
    left: 190px;
    top: 47px;
    width: 237px;
    height: 287px;
  }
  .label__variety {
    position: absolute;
    left: 0;
    right: 0;
    top: 343px;
    font-size: 25px;
    font-weight: 500;
    letter-spacing: 2.5px;
    line-height: 1;
  }
  .label__brand {
    position: absolute;
    left: 0;
    right: 0;
    top: 422px;
    margin: 0;
    font-size: 94px;
    font-weight: 500;
    letter-spacing: 3px;
    line-height: 88px;
  }
  .label__brand span { display: block; }
  .label__tagline {
    position: absolute;
    left: 0;
    right: 0;
    top: 616px;
    font-size: 17.5px;
    font-weight: 600;
    letter-spacing: 1.6px;
    line-height: 1;
  }
</style>
</head>
<body>
  <div class="canvas">
    <section class="label">
      <svg class="label__crest" viewBox="0 0 237 287" role="img" aria-label="Familienwappen: Schild mit drei Sternen, Reichsapfel mit Kreuz und Wolken">
        <path d="M2 2 H235 V190 Q230 240 118.5 285 Q7 240 2 190 Z" fill="var(--crest-fill)"/>
        <path d="M9 9 H228 V188 Q223 234 118.5 277 Q14 234 9 188 Z" fill="none" stroke="var(--crest-line)" stroke-width="1.5"/>
      </svg>
      <div class="label__variety">- LAGERBIER -</div>
      <h1 class="label__brand"><span>MOSTLY</span><span>GRAFUN</span></h1>
      <div class="label__tagline">BIERMANUFAKTUR WALLISER URSPRUNGS</div>
    </section>
  </div>
</body>
</html>
```